A start up Private Wine Label for export to Asia.

We are looking for the best graphic design for our very first wine label Corvessa Vineyards and would like the following requirements:

1. Black background - explore and play around the shade of black
2. Gold Shimmery Colour Font
3. Font should be a cursive classic posh that says Corvessa Vineyards
4. We would like the front graphic design to be simple and elegant and has a traditional classic feel to it.

Target Market(s)

Small scale to test the upper class market for export to Asia

Font styles to use
Script

Colors

Designer to choose colors to be used in the design.

Requirements
Must have
• Gold font for the label Corvessa Vineyards with shimmery touch to it.
• Elegant black background.
• Simple but elegant design.
• Attractive to the upper class market in Asia.
Nice to have
• Explore and play around with your imagination.

```html
<!DOCTYPE html>
<html lang="en">
<head>
<meta charset="utf-8">
<title>Corvessa Vineyards – Wine Label</title>
<link rel="stylesheet" href="https://fonts.googleapis.com/css2?family=Pinyon+Script&display=swap">
<style>
  :root {
    --canvas-bg: #eeece8;
    --label-black: #0b0b0c;
    --label-black-soft: #1c1c1e;
    --gold-deep: #8a6a1c;
    --gold-mid: #c9a53a;
    --gold-light: #f6e27a;
    --gold-glint: #fff5c2;
    --panel-navy: #2a3444;
    --panel-night: #0d1118;
  }

  * { margin: 0; padding: 0; box-sizing: border-box; }

  html, body {
    width: 1200px;
    height: 1200px;
    overflow: hidden;
    background: var(--canvas-bg);
  }

  .canvas {
    position: relative;
    width: 1200px;
    height: 1200px;
  }

  .wine-label {
    position: absolute;
    left: 160px;
    top: 100px;
    width: 880px;
    height: 1000px;
    box-shadow: 0 18px 40px rgba(0, 0, 0, 0.28);
  }

  .wine-label__art {
    position: absolute;
    inset: 0;
    width: 100%;
    height: 100%;
  }

  .brand-name {
    position: absolute;
    left: 0;
    width: 100%;
    text-align: center;
    font-family: "Pinyon Script", cursive;
    line-height: 1;
    background: linear-gradient(100deg,
      var(--gold-deep) 0%,
      var(--gold-light) 22%,
      var(--gold-mid) 40%,
      var(--gold-glint) 55%,
      var(--gold-mid) 72%,
      var(--gold-light) 88%,
      var(--gold-deep) 100%);
    -webkit-background-clip: text;
    background-clip: text;
    color: transparent;
  }

  .brand-name--first {
    top: 388px;
    font-size: 108px;
    letter-spacing: 2px;
  }

  .brand-name--second {
    top: 528px;
    font-size: 96px;
    padding-left: 40px;
    letter-spacing: 1px;
  }
</style>
</head>
<body>
<main class="canvas">
  <section class="wine-label" aria-label="Corvessa Vineyards wine label">
    <svg class="wine-label__art" viewBox="0 0 880 1000" aria-hidden="true">
      <defs>
        <linearGradient id="label-black" x1="0" y1="0" x2="1" y2="0">
          <stop offset="0" stop-color="#050505"/>
          <stop offset="0.18" stop-color="#1c1c1e"/>
          <stop offset="0.35" stop-color="#0a0a0b"/>
          <stop offset="0.55" stop-color="#202023"/>
          <stop offset="0.75" stop-color="#0b0b0c"/>
          <stop offset="1" stop-color="#18181a"/>
        </linearGradient>
        <linearGradient id="gold-band" x1="0" y1="0" x2="1" y2="0">
          <stop offset="0" stop-color="#8a6a1c"/>
          <stop offset="0.15" stop-color="#e8cc5c"/>
          <stop offset="0.3" stop-color="#b38a26"/>
          <stop offset="0.48" stop-color="#fff3b0"/>
          <stop offset="0.62" stop-color="#c9a53a"/>
          <stop offset="0.8" stop-color="#f6e27a"/>
          <stop offset="1" stop-color="#9a7420"/>
        </linearGradient>
        <linearGradient id="gold-band-sheen" x1="0" y1="0" x2="0" y2="1">
          <stop offset="0" stop-color="#fff" stop-opacity="0.35"/>
          <stop offset="0.5" stop-color="#fff" stop-opacity="0"/>
          <stop offset="1" stop-color="#000" stop-opacity="0.25"/>
        </linearGradient>
        <linearGradient id="gold-frame" x1="0" y1="0" x2="1" y2="1">
          <stop offset="0" stop-color="#f6e27a"/>
          <stop offset="0.3" stop-color="#a67c1f"/>
          <stop offset="0.5" stop-color="#fff5c2"/>
          <stop offset="0.7" stop-color="#c9a53a"/>
          <stop offset="1" stop-color="#f0d56a"/>
        </linearGradient>
        <linearGradient id="panel-fill" x1="0" y1="0" x2="1" y2="1">
          <stop offset="0" stop-color="#3a4658"/>
          <stop offset="0.45" stop-color="#1e2633"/>
          <stop offset="1" stop-color="#0d1118"/>
        </linearGradient>
        <linearGradient id="panel-gloss" x1="0" y1="0" x2="1" y2="1">
          <stop offset="0" stop-color="#fff" stop-opacity="0.16"/>
          <stop offset="0.5" stop-color="#fff" stop-opacity="0.04"/>
          <stop offset="0.51" stop-color="#fff" stop-opacity="0"/>
        </linearGradient>
        <linearGradient id="rule-gold" x1="0" y1="0" x2="1" y2="0">
          <stop offset="0" stop-color="#c9a53a" stop-opacity="0"/>
          <stop offset="0.2" stop-color="#e8cc5c"/>
          <stop offset="0.8" stop-color="#e8cc5c"/>
          <stop offset="1" stop-color="#c9a53a" stop-opacity="0"/>
        </linearGradient>
      </defs>

      <!-- label body -->
      <rect class="label-body" x="0" y="0" width="880" height="1000" fill="url(#label-black)"/>

      <!-- gold bands -->
      <g class="gold-band gold-band--top">
        <rect x="0" y="49" width="880" height="70" fill="url(#gold-band)"/>
        <rect x="0" y="49" width="880" height="70" fill="url(#gold-band-sheen)"/>
      </g>
      <g class="gold-band gold-band--bottom">
        <rect x="0" y="882" width="880" height="70" fill="url(#gold-band)"/>
        <rect x="0" y="882" width="880" height="70" fill="url(#gold-band-sheen)"/>
      </g>

      <!-- cartouche -->
      <g class="cartouche" transform="translate(38 241)">
        <path class="cartouche__outer"
              d="M60,70 Q402,-30 745,70 L745,110 L805,110 L805,415 L745,415 L745,455 Q402,555 60,455 L60,415 L0,415 L0,110 L60,110 Z"
              fill="url(#panel-fill)" stroke="url(#gold-frame)" stroke-width="16" stroke-linejoin="miter"/>
        <path class="cartouche__gloss"
              d="M60,70 Q402,-30 745,70 L745,110 L805,110 L805,415 L745,415 L745,455 Q402,555 60,455 L60,415 L0,415 L0,110 L60,110 Z"
              fill="url(#panel-gloss)"/>
        <path class="cartouche__inner"
              d="M85,94 Q402,6 720,94 L720,134 L775,134 L775,391 L720,391 L720,431 Q402,519 85,431 L85,391 L30,391 L30,134 L85,134 Z"
              fill="none" stroke="url(#gold-frame)" stroke-width="4"/>
      </g>

      <!-- fine gold rules -->
      <rect class="rule rule--top" x="190" y="370" width="500" height="3" fill="url(#rule-gold)"/>
      <rect class="rule rule--bottom" x="190" y="652" width="500" height="3" fill="url(#rule-gold)"/>
    </svg>

    <h1 class="brand-name brand-name--first">Corvessa</h1>
    <p class="brand-name brand-name--second">Vineyards</p>
  </section>
</main>
</body>
</html>
```